Self-Deprecating Marketing Guy Needs Blog Design (And Better Jokes)

For the past two years, I've been busy launching my own marketing agency based in New York City. Along the way, I meet countless folks who ask me about my "personal website." Personally, my "website" is usually Quipwire or TheHarborlamp.example, but that's neither here nor there. I'm looking to finally start blogging, like a real adult, but I don't have time to approach the project, and I don't want to give it to someone on my staff.

I'm a simple man, an old soul. I'm just looking for a site where I can blog. It'll be a one page site (probably ten posts per page, back/forward nav button at bottom), small nav column on left or right side with a photo (maybe, I have a face for radio), links to social, brief bio. Maybe pulling in my latest Chirp or jam (from SpinMyTuneNow.example).

Things to think about when you design:
-I love things that are big and bold
-I love travel, books, and film
-I love old maps (like this one: http://brantwoodmanor.example/images/Maps_Page_1.png)
-When it comes to color palettes, I usually like earth tones on the web, or go the other way and embrace color with a whole heart. Just don't end up in the middle.
-This is also nice (http://quillmarrowblog.example/)
-What I mean when I say Earth Tones (http://plainstitch.example/)

Always happy to give more detail

Industry/Entity Type

Marketing

Requirements
Must have
• -Template appropriate social icons (Chirpnet, KB, WorkRoster, SpinMyTuneNow)
Should not have
• -Anything tacky
• -Photos of Mr. Pudd

```html
<!DOCTYPE html>
<html lang="en">
<head>
<meta charset="utf-8">
<title>Dorian Pell — Blogging on all things marketing</title>
<link rel="stylesheet" href="https://fonts.googleapis.com/css2?family=Josefin+Sans:wght@600;700&family=Lato:wght@400;700&family=Merriweather:wght@700&display=swap">
<style>
  :root {
    --bar-dark: #434343;
    --bar-light: #ffffff;
    --page-bg: #cec7bf;
    --card: #ffffff;
    --ink: #444444;
    --ink-soft: #8a8a8a;
    --nav-ink: #6b6b6b;
    --accent: #3fa9d8;
    --pin: #a9d8ea;
  }
  * { box-sizing: border-box; margin: 0; padding: 0; }
  html, body { width: 1200px; height: 567px; overflow: hidden; }
  body {
    position: relative;
    background: radial-gradient(ellipse at 30% 40%, #d6d0c8 0%, var(--page-bg) 60%, #c6bfb6 100%);
    font-family: "Lato", sans-serif;
    color: var(--ink);
  }
  .site-header {
    position: absolute; left: 0; top: 0; width: 1200px; height: 57px;
    background: var(--bar-dark);
  }
  .site-title {
    position: absolute; left: 115px; top: 14px;
    font-family: "Josefin Sans", sans-serif; font-weight: 700;
    font-size: 28px; color: #fff; letter-spacing: 0.3px;
  }
  .site-tagline {
    position: absolute; left: 324px; top: 25px;
    font-family: Verdana, "Lato", sans-serif; font-size: 15px; color: #fff;
  }
  .social-links {
    position: absolute; right: 118px; top: 20px;
    display: flex; gap: 12px; list-style: none;
  }
  .social-links li {
    font-family: "Lato", sans-serif; font-weight: 700; font-size: 11px; color: #fff;
  }
  .main-nav {
    position: absolute; left: 0; top: 57px; width: 1200px; height: 38px;
    background: var(--bar-light);
  }
  .nav-active-line {
    position: absolute; left: 112px; top: 0; width: 114px; height: 3px;
    background: var(--accent);
  }
  .nav-menu {
    position: absolute; left: 125px; top: 12px;
    display: flex; list-style: none;
    font-size: 13px; color: var(--nav-ink);
  }
  .nav-menu li { margin-right: 28px; }
  .nav-menu li::after { content: "⌄"; font-size: 10px; margin-left: 6px; position: relative; top: -2px; }
  .search-icon { position: absolute; left: 1062px; top: 9px; }
  .post-card {
    position: absolute; left: 113px; top: 120px; width: 640px; height: 460px;
    background: var(--card); border-radius: 2px;
  }
  .post-title {
    position: absolute; left: 37px; top: 21px;
    font-family: "Josefin Sans", sans-serif; font-weight: 700;
    font-size: 27px; color: var(--ink);
  }
  .post-meta {
    position: absolute; left: 37px; top: 56px;
    font-size: 11.5px; color: var(--ink-soft); word-spacing: 2px;
  }
  .post-meta .sep { margin: 0 10px; }
  .pin-icon { position: absolute; left: 588px; top: 40px; }
  .post-image {
    position: absolute; left: 0; top: 100px; width: 640px; height: 295px;
    background: linear-gradient(180deg, #6fc7dd 0%, #7fd0e2 45%, #4fb4d6 55%, #5aa9c9 100%);
  }
  .post-excerpt {
    position: absolute; left: 42px; top: 431px;
    font-size: 14.5px; color: var(--ink);
  }
  .featured-card {
    position: absolute; left: 779px; top: 120px; width: 308px; height: 207px;
    border-radius: 2px; overflow: hidden;
    background: linear-gradient(180deg, #456a86 0%, #6c7f5a 45%, #7d8f4e 70%, #5a7b86 100%);
  }
  .featured-label {
    position: absolute; left: 0; top: 54px; width: 100%; text-align: center;
    font-family: "Merriweather", serif; font-weight: 700; font-size: 25px; color: #fff;
    text-shadow: 0 1px 3px rgba(0,0,0,0.35);
  }
  .profile-card {
    position: absolute; left: 779px; top: 353px; width: 308px; height: 230px;
    background: var(--card); border-radius: 2px; overflow: hidden;
  }
  .profile-cover {
    position: absolute; left: 0; top: 0; width: 308px; height: 146px;
    background: linear-gradient(180deg, #6ec2d8 0%, #e79a58 30%, #d9733f 70%, #c86a3e 100%);
  }
  .profile-avatar {
    position: absolute; left: 114px; top: 110px; width: 80px; height: 80px;
    border-radius: 50%; border: 4px solid #fff;
    background: radial-gradient(circle at 50% 45%, #6f7d62 0%, #3f4a3a 100%);
  }
  .profile-name {
    position: absolute; left: 0; top: 183px; width: 100%; text-align: center;
    font-family: "Josefin Sans", sans-serif; font-weight: 700; font-size: 27px; color: var(--ink);
  }
</style>
</head>
<body>
  <header class="site-header">
    <div class="site-title">Dorian Pell</div>
    <div class="site-tagline">Blogging on all things marketing</div>
    <ul class="social-links">
      <li>KB</li>
      <li>Chirpnet</li>
      <li>Lenscap</li>
    </ul>
  </header>

  <nav class="main-nav">
    <span class="nav-active-line"></span>
    <ul class="nav-menu">
      <li>Blog Layouts</li>
      <li>Page Layouts</li>
      <li>Features</li>
    </ul>
    <svg class="search-icon" width="22" height="22" viewBox="0 0 22 22" aria-label="Search">
      <circle cx="9" cy="9" r="6.5" fill="none" stroke="#6b6b6b" stroke-width="2.6"/>
      <line x1="13.8" y1="13.8" x2="19.5" y2="19.5" stroke="#6b6b6b" stroke-width="3" stroke-linecap="round"/>
    </svg>
  </nav>

  <article class="post-card">
    <h1 class="post-title">Marketing Made Easy</h1>
    <p class="post-meta">20. Aug<span class="sep">/</span>Uncategorized<span class="sep">/</span>5 Comments</p>
    <svg class="pin-icon" width="16" height="22" viewBox="0 0 16 22" aria-label="Pinned post">
      <path d="M4 1h8v2l-1.5 1v5l3.5 3v1.5H2V12l3.5-3V4L4 3z" fill="var(--pin)"/>
      <rect x="7.2" y="13.5" width="1.6" height="7" fill="var(--pin)"/>
    </svg>
    <div class="post-image" role="img" aria-label="Low-poly illustration of an iceberg in blue water"></div>
    <p class="post-excerpt">Hi! Welcome to our theme “Serene”. We worked our butts of making this Premium</p>
  </article>

  <aside>
    <div class="featured-card">
      <div role="img" aria-label="Low-poly illustration of green mountains and a river" style="position:absolute;inset:0;"></div>
      <div class="featured-label">A Featured Post</div>
    </div>
    <section class="profile-card">
      <div class="profile-cover" role="img" aria-label="Low-poly illustration of orange canyon and river"></div>
      <div class="profile-avatar" role="img" aria-label="Author portrait"></div>
      <h2 class="profile-name">Dorian Pell</h2>
    </section>
  </aside>
</body>
</html>
```